Corvane Supplies Business Card

Professional business card that stand out to our potential customers. Front and back with clean modern design

Industry/Entity Type

Oil and gas

Contact Information for Business Card

Name, address, website , office phone and cell number

Requirements
Must have
• Editable files for each employee

```html
<!DOCTYPE html>
<html lang="en">
<head>
<meta charset="utf-8">
<title>Corvane Supplies – Business Card</title>
<link rel="stylesheet" href="https://fonts.googleapis.com/css2?family=Nunito:wght@400;600;700;800&display=swap">
<style>
  :root {
    --page: #ffffff;
    --card: #1c1c1c;
    --cyan: #00acd0;
    --red: #ff0000;
    --ink: #1c1c1c;
  }
  * { margin: 0; padding: 0; box-sizing: border-box; }
  html, body {
    width: 1200px; height: 1200px; overflow: hidden;
    background: var(--page);
    font-family: "Nunito", sans-serif;
  }
  .canvas { position: relative; width: 1200px; height: 1200px; }
  .card {
    position: absolute; left: 181px; width: 845px; height: 482px;
    background: var(--card); color: var(--cyan);
  }
  .card--front { top: 94px; }
  .card--back { top: 630px; }

  .brand-mark { position: absolute; background: var(--red); }
  .brand-name {
    position: absolute; color: var(--cyan);
    font-weight: 800; letter-spacing: 0.06em; text-transform: uppercase;
    white-space: nowrap;
  }

  .card--front .brand-mark { left: 382px; top: 150px; width: 80px; height: 80px; }
  .card--front .brand-name { left: 0; width: 845px; text-align: center; top: 312px; font-size: 30px; }
  .card--front .website { position: absolute; right: 41px; top: 436px; font-size: 19px; letter-spacing: 0.04em; }

  .card--back .accent-bar { position: absolute; left: 0; top: 204px; width: 15px; height: 74px; background: var(--red); }
  .card--back .brand-mark { left: 629px; top: 100px; width: 64px; height: 64px; }
  .card--back .brand-name { left: 514px; width: 256px; text-align: center; top: 226px; font-size: 24px; }
  .person-name { position: absolute; left: 75px; top: 196px; font-size: 38px; font-weight: 700; letter-spacing: 0.14em; line-height: 1; }
  .person-title { position: absolute; left: 75px; top: 244px; font-size: 22px; font-weight: 700; line-height: 1; }
  .divider { position: absolute; left: 75px; top: 292px; width: 695px; height: 3px; background: var(--cyan); }

  .contacts { position: absolute; left: 75px; top: 318px; list-style: none; }
  .contacts li { display: flex; align-items: center; height: 26px; margin-bottom: 7px; font-size: 19px; letter-spacing: 0.03em; }
  .contacts .icon { width: 26px; height: 26px; margin-right: 15px; flex: none; }
  .contacts .phone { letter-spacing: 0.12em; }

  .address { position: absolute; right: 75px; top: 382px; font-size: 19px; }
</style>
</head>
<body>
<main class="canvas">

  <section class="card card--front" aria-label="Card front">
    <span class="brand-mark"></span>
    <span class="brand-name">Corvane Supplies</span>
    <span class="website">www.yourwebsite.com</span>
  </section>

  <section class="card card--back" aria-label="Card back">
    <span class="accent-bar"></span>
    <span class="brand-mark"></span>
    <span class="brand-name">Corvane Supplies</span>

    <h1 class="person-name">Your Name</h1>
    <p class="person-title">Your Title</p>
    <span class="divider"></span>

    <ul class="contacts">
      <li>
        <svg class="icon" viewBox="0 0 26 26" aria-hidden="true">
          <circle cx="13" cy="13" r="13" fill="#00acd0"/>
          <path d="M8 7.5l2.6-0.8 1.6 3.2-1.5 1.2c0.8 1.7 2 2.9 3.7 3.7l1.2-1.5 3.2 1.6-0.8 2.6c-5.4 0.3-10.3-4.6-10-10z" fill="#1c1c1c"/>
        </svg>
        <span class="phone">123-456-789</span>
      </li>
      <li>
        <svg class="icon" viewBox="0 0 26 26" aria-hidden="true">
          <circle cx="13" cy="13" r="13" fill="#00acd0"/>
          <g fill="none" stroke="#1c1c1c" stroke-width="1.3">
            <circle cx="13" cy="13" r="7"/>
            <ellipse cx="13" cy="13" rx="3" ry="7"/>
            <line x1="6" y1="13" x2="20" y2="13"/>
            <line x1="7.2" y1="9.5" x2="18.8" y2="9.5"/>
            <line x1="7.2" y1="16.5" x2="18.8" y2="16.5"/>
          </g>
        </svg>
        <span>www.yourwebsite.com</span>
      </li>
      <li>
        <svg class="icon" viewBox="0 0 26 26" aria-hidden="true">
          <circle cx="13" cy="13" r="13" fill="#00acd0"/>
          <g fill="none" stroke="#1c1c1c" stroke-width="1.3">
            <rect x="7" y="9" width="12" height="8.5"/>
            <path d="M7 9l6 5 6-5M7 17.5l4.5-4.5M19 17.5l-4.5-4.5"/>
          </g>
        </svg>
        <span>email@info.com</span>
      </li>
    </ul>

    <p class="address">Your Address and Country</p>
  </section>

</main>
</body>
</html>
```